Brightwell - Self Development Mobile App

Basic Instructions
1. please create an android app screen design for me, in figma, for my new app “Brightwell” based on this pencil drawing (Subjects.jpg)
2. Create the color pallet based on the colors of the logo (#fcd354 and #5dc9b7) and also add shades based on these colors based on material design.
3. the background should be white.
4. Use material design
Get Inspired by wordhopper design and calmnest design
These are the directions i provided for the programmer on how this screen will work:
top bar:
back icon on left (show if you are in a category and press to go back one category)
name of the field in middle in bold
share icon for sharing the current subject on the right before the drop down menu
3 dot icon on the right (drop down menu)
2nd top bar:
fire icon on left for streak (how many days straight did you do a lesson)
star icon a bit after it (how many lessons did you pass)
circles section:
each category will get a section
each category will have a small star with a number that shows how many stars the user has from that category
each category will have an icon before it
under each category there will be circles for all the subjects under that category
scroll horizontally to see more subjects
each subject will have the amount stars gained from it (like the circles of the fields in the fields screen)
scroll down to see more fields with their subjects
note that the order of the subjects and categories should be based on the practial/spiritual score that the user has been assigned based on the initial wizard
More Notes
1. the scribbles in the circles under the following categories (Dreams, Sub-Concious, Feeling)) are just place filers. Please add example content based on the content in the circles that are under “Memory” category
2. There are more sections after Feeling so users should be able to scroll down to see more sections
3. There are more categories to the right so under each section
Final Thoughts
Maybe its better to have rounded cornered squares instead of circles. You choose what you think is best.
After you have created the Subjects screen and I like it, then I'll give you instructions for the other 5 screens.
Target Market(s)
general public, adults 18-80
Font styles to use
Look and feel
Each slider illustrates characteristics of the customer's brand and the style your logo design should communicate.

```html
<!DOCTYPE html>
<html lang="en">
<head>
<meta charset="utf-8">
<title>Brightwell – App Screens</title>
<link rel="stylesheet" href="https://fonts.googleapis.com/css2?family=Urbanist:wght@400;500;600;700&display=swap">
<style>
:root{
  --yellow:#fcd354;
  --teal:#5dc9b7;
  --teal-dark:#3aa896;
  --bg:#0b1110;
  --bar:#121b1a;
  --pill:#1a2322;
  --ink:#101514;
  --white:#ffffff;
  --mint:#e8faf6;
  --line:#2a3332;
}
*{box-sizing:border-box;margin:0;padding:0}
html,body{width:1200px;height:885px;overflow:hidden;background:#fff;font-family:"Urbanist",sans-serif}
.stage{position:absolute;left:0;top:0;width:1360px;height:1003px;transform:scale(0.8824);transform-origin:0 0}
.screen{position:absolute;top:31px;width:414px;height:895px;background:var(--bg);overflow:hidden;box-shadow:0 4px 14px rgba(0,0,0,.35);color:var(--white)}
.status{height:18px;background:#0f1716;display:flex;justify-content:flex-end;align-items:center;gap:6px;padding-right:24px}
.status i{display:block;width:5px;height:9px;background:#ddd;border-radius:1px}
.status b{display:block;width:9px;height:9px;border-left:2px solid #ddd;border-bottom:2px solid #ddd}
.topbar{height:74px;background:var(--bar);position:relative;display:flex;align-items:center}
.topbar .title{position:absolute;left:0;right:0;text-align:center;font-size:23px;font-weight:600}
.topbar .back{position:absolute;left:22px;top:24px;width:28px;height:28px}
.topbar .share{position:absolute;right:62px;top:25px;width:24px;height:24px}
.topbar .more{position:absolute;right:18px;top:24px;width:20px;height:28px}
.brand{display:flex;align-items:center;gap:14px;padding-left:24px}
.brand-dot{width:36px;height:36px;border-radius:50%;background:var(--yellow)}
.brand-name{font-size:23px;font-weight:600}
.stats{position:absolute;display:flex;align-items:center;gap:8px;font-size:20px;font-weight:500}
.stats svg{width:26px;height:28px}
.stats .gap{width:14px}
.abs{position:absolute}
.tile{position:absolute;width:103px;height:101px;border-radius:14px;background:var(--yellow);color:var(--ink);text-align:center}
.tile .ic{position:absolute;left:50%;top:12px;width:40px;height:40px;transform:translateX(-50%)}
.tile .lbl{position:absolute;left:0;right:0;top:55px;font-size:13px;font-weight:500}
.badge{position:absolute;right:8px;bottom:-8px;height:19px;padding:0 9px;border-radius:10px;background:var(--pill);color:#fff;font-size:12px;font-weight:600;display:flex;align-items:center;gap:6px}
.badge svg{width:13px;height:13px}
.pick{position:absolute;left:50%;bottom:1px;transform:translateX(-50%);height:19px;min-width:38px;padding:0 8px;border-radius:10px;background:var(--pill);color:#fff;font-size:12px;font-weight:600;display:flex;align-items:center;justify-content:center;gap:7px;white-space:nowrap}
.pick .ok{width:12px;height:12px;border-radius:3px;background:var(--teal);display:flex;align-items:center;justify-content:center}
.pick .ok svg{width:9px;height:9px}
.tile.active{background:var(--mint);outline:2px solid var(--mint);outline-offset:3px}
.tile.faded{opacity:.25}
.me{position:absolute;width:116px;height:114px;border-radius:14px;background:var(--teal);color:var(--ink);font-size:30px;font-weight:600;display:flex;align-items:center;justify-content:center}
.greet{position:absolute;left:23px;top:190px;font-size:15px}
.headline{position:absolute;left:23px;top:214px;font-size:22px;font-weight:600}
.divider{position:absolute;left:0;right:0;height:1px;background:var(--line)}
.cat{position:absolute;left:24px;display:flex;align-items:center;gap:12px;font-size:23px;font-weight:600}
.cat .cat-ic{width:34px;height:34px}
.cat .count{display:flex;align-items:center;gap:8px;font-size:15px;font-weight:500;margin-left:4px}
.cat .count svg{width:24px;height:24px}
.subj{position:absolute;width:103px;height:101px;border-radius:12px;background:var(--white);overflow:hidden}
.subj .art{position:absolute;left:0;right:0;top:0;height:80px}
.subj .art.brain{background:linear-gradient(135deg,#fce9d8,#f7b9b0 50%,#8fd3c8)}
.subj .art.name{background:linear-gradient(180deg,#fde3c4,#f9d6b3)}
.subj .art.nums{background:linear-gradient(135deg,#8fdb8f,#5a8fd6 55%,#e97a7a)}
.subj .art.logic{background:linear-gradient(135deg,#fbd3d9,#cfeee8)}
.subj .tag{position:absolute;left:-1px;right:-1px;top:42px;height:25px;border-radius:13px;background:var(--teal);color:#fff;font-size:12px;font-weight:500;display:flex;align-items:center;justify-content:center;white-space:nowrap}
.subj .sbadge{position:absolute;left:50%;transform:translateX(-50%);bottom:2px;height:17px;padding:0 9px;border-radius:9px;background:var(--pill);color:#fff;font-size:12px;font-weight:600;display:flex;align-items:center;gap:6px}
.subj .sbadge svg{width:13px;height:13px}
.you{position:absolute;left:24px;top:128px;font-size:38px;font-weight:500}
.nav{position:absolute;left:0;right:0;bottom:0;height:76px;background:var(--bar);border-radius:16px 16px 0 0;display:flex;justify-content:space-between;padding:0 24px}
.nav a{display:flex;flex-direction:column;align-items:center;justify-content:center;gap:4px;font-size:13px;color:#fff;text-decoration:none;width:60px}
.nav svg{width:28px;height:28px}
.progress{position:absolute;left:24px;right:24px;top:115px;height:20px;border-radius:10px;background:var(--yellow)}
.progress span{display:block;width:100px;height:12px;margin:4px 0 0 6px;border-radius:6px;background:var(--teal)}
.wizard-brand{position:absolute;left:0;right:0;top:186px;display:flex;justify-content:center;align-items:center;gap:16px}
.prompt{position:absolute;left:0;right:0;top:262px;text-align:center;font-size:19px;font-weight:500;line-height:34px}
.fab{position:absolute;left:349px;top:762px;width:42px;height:42px;border-radius:50%;background:var(--teal);display:flex;align-items:center;justify-content:center}
.fab svg{width:24px;height:24px}
</style>
</head>
<body>
<svg width="0" height="0" style="position:absolute">
  <defs>
    <symbol id="i-star" viewBox="0 0 24 24"><path d="M12 1l2.6 6.4 6.9-2.1-3.8 6 4.9 5.3-7.1.3L12 23l-3.5-6.1-7.1-.3 4.9-5.3-3.8-6 6.9 2.1z" fill="currentColor"/></symbol>
    <symbol id="i-flame" viewBox="0 0 24 28"><path d="M12 1c1 5 8 8 8 16a8 8 0 0 1-16 0c0-4 2-6 3-8 1 3 2 4 3 4 0-5 1-9 2-12z" fill="#fcd354"/><path d="M12 14c1 3 4 4 4 8a4 4 0 0 1-8 0c0-2 1-3 2-4 1 1 1 1 2 1 0-2 0-3 0-5z" fill="#5dc9b7"/></symbol>
    <symbol id="i-mind" viewBox="0 0 40 40"><path d="M20 4c-8 0-13 6-13 13 0 4 2 7 4 9v10h13v-5h5c2 0 3-1 3-3v-4l3-1-3-6c0-8-5-13-12-13z" fill="currentColor"/><circle cx="19" cy="16" r="4" fill="#fcd354"/></symbol>
    <symbol id="i-check" viewBox="0 0 40 40"><path d="M20 2l5 4 6-1 2 6 5 3-2 6 2 6-5 3-2 6-6-1-5 4-5-4-6 1-2-6-5-3 2-6-2-6 5-3 2-6 6 1z" fill="currentColor"/><path d="M12 20l6 6 11-12" stroke="#fcd354" stroke-width="4" fill="none"/></symbol>
    <symbol id="i-body" viewBox="0 0 40 40"><circle cx="20" cy="6" r="4" fill="currentColor"/><path d="M6 12h28v5H24v19h-5v-10h-1v10h-4V17H6z" fill="currentColor"/></symbol>
    <symbol id="i-heart" viewBox="0 0 40 40"><path d="M8 3h24v34l-12-8-12 8z" fill="currentColor"/><path d="M20 19l-5-5a3 3 0 0 1 5-3 3 3 0 0 1 5 3z" fill="#fcd354"/></symbol>
    <symbol id="i-bag" viewBox="0 0 40 40"><path d="M10 4h20l-4 7h-12z" fill="currentColor"/><path d="M14 13h12c6 4 10 10 10 16 0 6-5 8-16 8S4 35 4 29c0-6 4-12 10-16z" fill="currentColor"/><circle cx="20" cy="26" r="5" fill="#fcd354"/></symbol>
    <symbol id="i-hands" viewBox="0 0 40 40"><path d="M18 3l-2 18-8 10v6h10V22zM22 3l2 18 8 10v6H22V22z" fill="currentColor"/><path d="M4 30l6-10v12zM36 30l-6-10v12z" fill="currentColor"/></symbol>
    <symbol id="i-group" viewBox="0 0 40 40"><circle cx="20" cy="11" r="5" fill="currentColor"/><circle cx="8" cy="15" r="4" fill="currentColor"/><circle cx="32" cy="15" r="4" fill="currentColor"/><path d="M11 30c0-6 4-10 9-10s9 4 9 10zM1 30c0-5 3-8 7-8 2 0 3 1 4 2-2 2-3 4-3 6zM39 30c0-5-3-8-7-8-2 0-3 1-4 2 2 2 3 4 3 6z" fill="currentColor"/></symbol>
    <symbol id="i-medal" viewBox="0 0 40 40"><circle cx="20" cy="15" r="12" fill="none" stroke="currentColor" stroke-width="3.5"/><path d="M20 9l2 4.5 4.5.4-3.4 3 1 4.6L20 19l-4.1 2.5 1-4.6-3.4-3 4.5-.4z" fill="currentColor"/><path d="M13 26l-2 12 9-5 9 5-2-12" fill="currentColor"/></symbol>
    <symbol id="i-brain" viewBox="0 0 34 34"><path d="M17 4c-2-2-7-2-8 2-4 0-6 4-4 7-3 2-3 7 0 9 0 4 4 7 8 5 2 3 4 3 4 0V4zM17 4c2-2 7-2 8 2 4 0 6 4 4 7 3 2 3 7 0 9 0 4-4 7-8 5-2 3-4 3-4 0" fill="none" stroke="#fff" stroke-width="2.2"/></symbol>
    <symbol id="i-head" viewBox="0 0 34 34"><path d="M17 3C9 3 4 9 4 15c0 4 2 7 4 8v8h11v-4h4c2 0 3-1 3-3v-3l3-1-3-6C26 8 22 3 17 3z" fill="none" stroke="#fff" stroke-width="2.2"/><path d="M12 13c2-4 9-4 10 1 0 3-4 3-5 2" fill="none" stroke="#fff" stroke-width="2.2"/></symbol>
    <symbol id="i-spiral" viewBox="0 0 34 34"><path d="M17 3C9 3 4 9 4 15c0 4 2 7 4 8v8h11v-4h4c2 0 3-1 3-3v-3l3-1-3-6C26 8 22 3 17 3z" fill="none" stroke="#fff" stroke-width="2.2"/><path d="M16 16a2 2 0 1 1 3 1 5 5 0 1 1-6-4" fill="none" stroke="#fff" stroke-width="2.2"/></symbol>
    <symbol id="i-back" viewBox="0 0 28 28"><path d="M26 14H4M13 4L3 14l10 10" stroke="#fff" stroke-width="2.6" fill="none"/></symbol>
    <symbol id="i-share" viewBox="0 0 24 24"><circle cx="19" cy="4" r="3.5" fill="#5dc9b7"/><circle cx="5" cy="12" r="3.5" fill="#5dc9b7"/><circle cx="19" cy="20" r="3.5" fill="#5dc9b7"/><path d="M19 4L5 12l14 8" stroke="#5dc9b7" stroke-width="2.2" fill="none"/></symbol>
    <symbol id="i-more" viewBox="0 0 20 28"><circle cx="10" cy="4" r="2.8" fill="#fff"/><circle cx="10" cy="14" r="2.8" fill="#fff"/><circle cx="10" cy="24" r="2.8" fill="#fff"/></symbol>
    <symbol id="i-fields" viewBox="0 0 28 28"><path d="M9 2l6 10H3z" fill="#fcd354"/><rect x="3" y="15" width="10" height="10" fill="#fcd354"/><circle cx="21" cy="20" r="5" fill="#fcd354"/></symbol>
    <symbol id="i-explore" viewBox="0 0 28 28"><path d="M11 2l6 10H5z" fill="#fcd354"/><rect x="5" y="15" width="8" height="8" fill="#fcd354"/><circle cx="19" cy="19" r="4" fill="none" stroke="#fcd354" stroke-width="2.4"/><path d="M22 22l4 4" stroke="#fcd354" stroke-width="2.4"/></symbol>
    <symbol id="i-account" viewBox="0 0 28 28"><circle cx="14" cy="14" r="12" fill="none" stroke="#fcd354" stroke-width="2.4"/><circle cx="14" cy="11" r="4.5" fill="#fcd354"/><path d="M6 22c2-4 5-5 8-5s6 1 8 5" fill="#fcd354"/></symbol>
    <symbol id="i-tick" viewBox="0 0 10 10"><path d="M1.5 5l2.5 2.5L8.5 2" stroke="#1a2322" stroke-width="1.8" fill="none"/></symbol>
    <symbol id="i-horn" viewBox="0 0 24 24"><path d="M3 9h4l10-6v18L7 15H3z" fill="#fff"/><path d="M6 15l2 6h3l-1-6" fill="#fff"/><path d="M20 8v8" stroke="#fff" stroke-width="2"/></symbol>
  </defs>
</svg>

<div class="stage">

  <!-- Fields screen -->
  <section class="screen" style="left:31px">
    <div class="status"><i></i><b></b></div>
    <header class="topbar">
      <div class="brand"><span class="brand-dot"></span><span class="brand-name">Brightwell</span></div>
    </header>
    <div class="stats" style="left:23px;top:138px">
      <svg><use href="#i-flame"/></svg>2d<span class="gap"></span>
      <svg style="color:var(--yellow)"><use href="#i-star"/></svg>34
    </div>
    <p class="greet">Good evening, Sam</p>
    <h1 class="headline">Let’s Start your Day</h1>

    <svg class="abs" style="left:0;top:0" width="414" height="700">
      <g stroke="#5dc9b7" stroke-width="2" stroke-dasharray="2 4" fill="none">
        <line x1="125" y1="420" x2="160" y2="450"/>
        <line x1="207" y1="420" x2="207" y2="441"/>
        <line x1="290" y1="420" x2="260" y2="450"/>
        <line x1="127" y1="499" x2="149" y2="499"/>
        <line x1="265" y1="499" x2="287" y2="499"/>
        <line x1="125" y1="580" x2="160" y2="552"/>
        <line x1="207" y1="555" x2="207" y2="576"/>
        <line x1="290" y1="580" x2="260" y2="552"/>
      </g>
    </svg>

    <div class="tile" style="left:24px;top:320px"><svg class="ic"><use href="#i-mind"/></svg><span class="lbl">Mind</span><span class="badge" style="right:8px;bottom:1px"><svg style="color:var(--teal)"><use href="#i-star"/></svg>3</span></div>
    <div class="tile" style="left:156px;top:320px"><svg class="ic"><use href="#i-check"/></svg><span class="lbl">Recomended</span><span class="badge" style="bottom:1px"><svg style="color:var(--teal)"><use href="#i-star"/></svg>5</span></div>
    <div class="tile active" style="left:287px;top:320px"><svg class="ic"><use href="#i-body"/></svg><span class="lbl">Body</span><span class="badge" style="bottom:1px"><svg style="color:var(--teal)"><use href="#i-star"/></svg>7</span></div>

    <div class="tile" style="left:24px;top:448px"><svg class="ic"><use href="#i-heart"/></svg><span class="lbl">Hobbies</span><span class="badge" style="bottom:1px"><svg style="color:var(--teal)"><use href="#i-star"/></svg>31</span></div>
    <div class="me" style="left:149px;top:441px">Me</div>
    <div class="tile" style="left:287px;top:448px"><svg class="ic"><use href="#i-bag"/></svg><span class="lbl">Finance</span><span class="badge" style="bottom:1px"><svg style="color:var(--teal)"><use href="#i-star"/></svg>12</span></div>

    <div class="tile" style="left:24px;top:576px"><svg class="ic"><use href="#i-hands"/></svg><span class="lbl">Spiritual</span><span class="badge" style="bottom:1px"><svg style="color:var(--teal)"><use href="#i-star"/></svg>5</span></div>
    <div class="tile" style="left:156px;top:576px"><svg class="ic"><use href="#i-group"/></svg><span class="lbl">Social</span><span class="badge" style="bottom:1px"><svg style="color:var(--teal)"><use href="#i-star"/></svg>8</span></div>
    <div class="tile" style="left:287px;top:576px"><svg class="ic"><use href="#i-medal"/></svg><span class="lbl">Professional</span><span class="badge" style="bottom:1px"><svg style="color:var(--teal)"><use href="#i-star"/></svg>16</span></div>

    <nav class="nav">
      <a href="#"><svg><use href="#i-fields"/></svg>Fields</a>
      <a href="#"><svg><use href="#i-explore"/></svg>Explore</a>
      <a href="#"><svg><use href="#i-account"/></svg>Account</a>
    </nav>
  </section>

  <!-- Subjects screen -->
  <section class="screen" style="left:471px">
    <div class="status"><i></i><b></b></div>
    <header class="topbar">
      <svg class="back"><use href="#i-back"/></svg>
      <span class="title">Mind</span>
      <svg class="share"><use href="#i-share"/></svg>
      <svg class="more"><use href="#i-more"/></svg>
    </header>
    <div class="you">You</div>
    <div class="stats" style="left:112px;top:140px">
      <svg><use href="#i-flame"/></svg>2d<span class="gap"></span>
      <svg style="color:var(--yellow);width:34px;height:34px"><use href="#i-star"/></svg>34
    </div>

    <div class="divider" style="top:231px"></div>
    <div class="cat" style="top:253px"><svg class="cat-ic"><use href="#i-brain"/></svg>Memory<span class="count"><svg style="color:var(--yellow)"><use href="#i-star"/></svg>7</span></div>
    <div class="subj" style="left:24px;top:314px"><div class="art brain" role="img" aria-label="Illustration of a brain with coloured blocks"></div><span class="tag">Basic memory</span><span class="sbadge"><svg style="color:var(--yellow)"><use href="#i-star"/></svg>3</span></div>
    <div class="subj" style="left:136px;top:314px"><div class="art name" role="img" aria-label="Illustration of a name tag"></div><span class="tag">Names call</span><span class="sbadge"><svg style="color:var(--yellow)"><use href="#i-star"/></svg>5</span></div>
    <div class="subj" style="left:249px;top:314px"><div class="art nums" role="img" aria-label="Illustration of numbered blocks"></div><span class="tag">Number guess</span><span class="sbadge"><svg style="color:var(--yellow)"><use href="#i-star"/></svg>12</span></div>
    <div class="subj" style="left:362px;top:314px"><div class="art logic" role="img" aria-label="Illustration of a logic puzzle"></div><span class="tag" style="justify-content:flex-start;padding-left:12px">Logical</span><span class="sbadge" style="left:40px"><svg style="color:var(--yellow)"><use href="#i-star"/></svg>4</span></div>

    <div class="divider" style="top:455px"></div>
    <div class="cat" style="top:482px"><svg class="cat-ic"><use href="#i-head"/></svg>Dreams<span class="count"><svg style="color:var(--yellow)"><use href="#i-star"/></svg>12</span></div>
    <div class="subj" style="left:24px;top:543px"><div class="art brain" role="img" aria-label="Illustration of a brain with coloured blocks"></div><span class="tag">Basic memory</span><span class="sbadge"><svg style="color:var(--yellow)"><use href="#i-star"/></svg>3</span></div>
    <div class="subj" style="left:136px;top:543px"><div class="art name" role="img" aria-label="Illustration of a name tag"></div><span class="tag">Names call</span><span class="sbadge"><svg style="color:var(--yellow)"><use href="#i-star"/></svg>5</span></div>
    <div class="subj" style="left:249px;top:543px"><div class="art nums" role="img" aria-label="Illustration of numbered blocks"></div><span class="tag">Number guess</span><span class="sbadge"><svg style="color:var(--yellow)"><use href="#i-star"/></svg>12</span></div>
    <div class="subj" style="left:362px;top:543px"><div class="art logic" role="img" aria-label="Illustration of a logic puzzle"></div><span class="tag" style="justify-content:flex-start;padding-left:12px">Logical</span><span class="sbadge" style="left:40px"><svg style="color:var(--yellow)"><use href="#i-star"/></svg>4</span></div>

    <div class="divider" style="top:684px"></div>
    <div class="cat" style="top:716px"><svg class="cat-ic"><use href="#i-spiral"/></svg>Sub-Concious<span class="count"><svg style="color:var(--yellow)"><use href="#i-star"/></svg>18</span></div>
    <div class="subj" style="left:24px;top:777px"><div class="art brain" role="img" aria-label="Illustration of a brain with coloured blocks"></div></div>
    <div class="subj" style="left:136px;top:777px"><div class="art name" role="img" aria-label="Illustration of a name tag"></div></div>
    <div class="subj" style="left:249px;top:777px"><div class="art nums" role="img" aria-label="Illustration of numbered blocks"></div></div>
    <div class="subj" style="left:362px;top:777px"><div class="art logic" role="img" aria-label="Illustration of a logic puzzle"></div></div>

    <nav class="nav">
      <a href="#"><svg><use href="#i-fields"/></svg>Fields</a>
      <a href="#"><svg><use href="#i-explore"/></svg>Explore</a>
      <a href="#"><svg><use href="#i-account"/></svg>Account</a>
    </nav>
  </section>

  <!-- Wizard screen -->
  <section class="screen" style="left:911px">
    <div class="status"><i></i><b></b></div>
    <header class="topbar">
      <svg class="back"><use href="#i-back"/></svg>
      <span class="title">Wizard</span>
      <svg class="share"><use href="#i-share"/></svg>
      <svg class="more"><use href="#i-more"/></svg>
    </header>
    <div class="progress"><span></span></div>
    <div class="wizard-brand"><span class="brand-dot"></span><span class="brand-name">Brightwell</span></div>
    <p class="prompt">Please choose 3 subjects that<br>interest you the most :</p>

    <div class="tile" style="left:24px;top:358px"><svg class="ic"><use href="#i-hands"/></svg><span class="lbl">Spiritual</span><span class="pick">Pick<span class="ok"><svg><use href="#i-tick"/></svg></span></span></div>
    <div class="tile" style="left:156px;top:358px"><svg class="ic"><use href="#i-group"/></svg><span class="lbl">Social</span><span class="pick">1<span class="ok"><svg><use href="#i-tick"/></svg></span></span></div>
    <div class="tile" style="left:287px;top:358px"><svg class="ic"><use href="#i-medal"/></svg><span class="lbl">Professional</span><span class="pick">Pick<span class="ok"><svg><use href="#i-tick"/></svg></span></span></div>

    <div class="tile" style="left:24px;top:488px"><svg class="ic"><use href="#i-mind"/></svg><span class="lbl">Mind</span><span class="pick">2<span class="ok"><svg><use href="#i-tick"/></svg></span></span></div>
    <div class="tile" style="left:156px;top:488px"><svg class="ic"><use href="#i-body"/></svg><span class="lbl">Body</span><span class="pick">Pick<span class="ok"><svg><use href="#i-tick"/></svg></span></span></div>
    <div class="tile" style="left:287px;top:488px"><svg class="ic"><use href="#i-bag"/></svg><span class="lbl">Finance</span><span class="pick">Pick<span class="ok"><svg><use href="#i-tick"/></svg></span></span></div>

    <div class="tile" style="left:24px;top:616px"><svg class="ic"><use href="#i-hands"/></svg><span class="lbl">Spiritual</span><span class="pick">Pick<span class="ok"><svg><use href="#i-tick"/></svg></span></span></div>
    <div class="tile" style="left:156px;top:616px"><svg class="ic"><use href="#i-group"/></svg><span class="lbl">Social</span><span class="pick">3<span class="ok"><svg><use href="#i-tick"/></svg></span></span></div>
    <div class="tile" style="left:287px;top:616px"><svg class="ic"><use href="#i-medal"/></svg><span class="lbl">Professional</span><span class="pick">Pick<span class="ok"><svg><use href="#i-tick"/></svg></span></span></div>

    <div class="tile faded" style="left:24px;top:746px"><svg class="ic"><use href="#i-mind"/></svg><span class="lbl">Mind</span></div>
    <div class="tile faded" style="left:156px;top:746px"><svg class="ic"><use href="#i-body"/></svg><span class="lbl">Body</span></div>
    <div class="tile faded" style="left:287px;top:746px"><svg class="ic"><use href="#i-bag"/></svg><span class="lbl">Finance</span></div>

    <div class="fab"><svg><use href="#i-horn"/></svg></div>

    <nav class="nav">
      <a href="#"><svg><use href="#i-fields"/></svg>Fields</a>
      <a href="#"><svg><use href="#i-explore"/></svg>Explore</a>
      <a href="#"><svg><use href="#i-account"/></svg>Account</a>
    </nav>
  </section>

</div>
</body>
</html>
```